Accounting Business needs double sided DL flyer design

We need a double sided DL flyer designed,
Front side with logo, web address and our short intro.
Backside to have a list of services.
Our colours are blue and a concrete grey colour. Look at our website for a feel for our colour scheme.
www.lanternwellgroup.com.au
I have included the pic from our website to possibly use but we are also open to new creative ideas.
Target Market(s)
Our target market are proactive business owners, particularly in the wine and hospitality industry.
Industry/Entity Type
Business
Look and feel

```html
<!DOCTYPE html>
<html lang="en">
<head>
<meta charset="utf-8">
<title>Lanternwell Group – DL Flyer</title>
<link rel="stylesheet" href="https://fonts.googleapis.com/css2?family=Open+Sans:wght@300;400;600;700&family=Fira+Sans+Condensed:wght@500;600;700&display=swap">
<style>
  :root {
    --brand-blue: #1c4584;
    --concrete-light: #eceded;
    --concrete-mid: #c9cacb;
    --concrete-dark: #8d8f91;
    --text-grey: #5a5d61;
    --list-grey: #6e7175;
    --white: #ffffff;
  }
  * { box-sizing: border-box; margin: 0; padding: 0; }
  html, body { width: 1200px; height: 1200px; overflow: hidden; background: var(--white); }
  body { font-family: "Open Sans", Arial, sans-serif; }

  .flyer { position: relative; width: 1200px; height: 1200px; }
  .side { position: absolute; left: 0; width: 1200px; height: 600px; overflow: hidden; }
  .side--front { top: 0; }
  .side--back { top: 600px; }

  .stairs-photo {
    position: absolute; inset: 0;
    background:
      linear-gradient(155deg, rgba(120,122,125,0) 0%, rgba(120,122,125,0) 35%, rgba(120,122,125,0.35) 55%, rgba(110,112,115,0.6) 100%),
      linear-gradient(90deg, var(--concrete-light) 0%, #e2e3e4 45%, var(--concrete-mid) 100%);
  }
  .wall-backdrop {
    position: absolute; inset: 0;
    background: linear-gradient(90deg, #f1f2f2 0%, #e8e9ea 50%, #d9dadb 100%);
  }

  .brand {
    position: absolute; left: 36px; top: 40px;
    display: flex; align-items: center; gap: 12px;
  }
  .brand__mark { width: 44px; height: 44px; background: var(--brand-blue); }
  .brand__name {
    font-weight: 700; font-size: 25px; letter-spacing: 2px; color: var(--brand-blue); line-height: 1;
  }
  .brand__tagline {
    margin-top: 6px; font-size: 8.5px; letter-spacing: 2.6px; color: var(--brand-blue); font-weight: 600;
  }

  .slogan { position: absolute; display: flex; align-items: flex-end; gap: 8px; }
  .slogan__lead {
    font-weight: 600; font-size: 21px; line-height: 28px; color: var(--text-grey);
    text-align: right; text-transform: uppercase;
    border-bottom: 2px solid var(--text-grey);
  }
  .slogan__key {
    font-family: "Fira Sans Condensed", "Open Sans", sans-serif;
    font-weight: 700; font-size: 44px; line-height: 1; color: var(--brand-blue);
    margin-bottom: 3px;
  }
  .slogan--success { right: 136px; top: 46px; }
  .slogan--reason { left: 498px; top: 244px; }
  .slogan--hand { left: 88px; top: 466px; }

  .contact {
    position: absolute; right: 62px; bottom: 17px;
    font-family: "Fira Sans Condensed", "Open Sans", sans-serif;
    font-weight: 600; font-size: 19px; color: var(--white);
    text-align: right; line-height: 33px;
  }
  .contact__row { display: flex; align-items: center; justify-content: flex-end; gap: 6px; }
  .contact__icon { width: 40px; height: 30px; }
  .accent-bar { position: absolute; background: var(--brand-blue); }
  .side--front .accent-bar { right: 0; top: 541px; width: 44px; height: 18px; }
  .side--back .accent-bar { left: 0; top: 542px; width: 1200px; height: 18px; }

  .services-title {
    position: absolute; left: 35px; top: 146px;
    font-weight: 700; font-size: 29px; color: var(--brand-blue); letter-spacing: 0.3px;
  }
  .services-title::after {
    content: ""; display: block; width: 30px; height: 2px; background: var(--text-grey); margin-top: 8px;
  }
  .services { position: absolute; top: 210px; list-style: none; }
  .services--left { left: 36px; width: 360px; }
  .services--right { left: 418px; width: 300px; }
  .services li {
    position: relative; padding-left: 28px; margin-bottom: 12.4px;
    font-weight: 400; font-size: 21.5px; line-height: 28px; color: var(--list-grey);
  }
  .services li::before {
    content: "›"; position: absolute; left: 0; top: -1px;
    font-weight: 700; font-size: 26px; color: var(--brand-blue);
  }

  .advisor-photo {
    position: absolute; left: 740px; top: 20px; width: 460px; height: 580px;
    background: linear-gradient(180deg, #d6d7d9 0%, #a9abae 35%, #55585d 70%, #2e3034 100%);
  }
  .side--back .accent-bar { z-index: 0; }
  .side--back .advisor-photo { z-index: 1; }
  .side--back .contact { z-index: 2; }
</style>
</head>
<body>
<main class="flyer">

  <section class="side side--front">
    <div class="stairs-photo" role="img" aria-label="Photograph of floating concrete stairs climbing a grey wall"></div>

    <div class="brand">
      <span class="brand__mark"></span>
      <div>
        <div class="brand__name">LANTERNWELL GROUP</div>
        <div class="brand__tagline">BUSINESS ADVISORS &amp; ACCOUNTANTS</div>
      </div>
    </div>

    <div class="slogan slogan--success">
      <span class="slogan__lead">A true<br>sounding<br>board for</span>
      <span class="slogan__key">success</span>
    </div>
    <div class="slogan slogan--reason">
      <span class="slogan__lead">A<br>voice<br>of</span>
      <span class="slogan__key">reason</span>
    </div>
    <div class="slogan slogan--hand">
      <span class="slogan__lead">A<br>guiding</span>
      <span class="slogan__key">hand</span>
    </div>

    <div class="accent-bar"></div>
    <div class="contact">
      <div class="contact__row">0400 318 762
        <svg class="contact__icon" viewBox="0 0 40 30" aria-hidden="true"><path d="M8 28 A16 16 0 0 1 30 4" fill="none" stroke="#6b6e72" stroke-width="3"/><path d="M20 24 L26 8 L31 10 L28 13 L24 22 Z" fill="#6b6e72"/></svg>
      </div>
      <div class="contact__row">www.lanternwellgroup.com.au
        <svg class="contact__icon" viewBox="0 0 40 30" aria-hidden="true"><path d="M8 29 A16 16 0 0 1 24 3" fill="none" stroke="#6b6e72" stroke-width="3"/><circle cx="26" cy="17" r="11" fill="none" stroke="#6b6e72" stroke-width="2.5"/><path d="M15 17 H37 M26 6 V28 M26 6 C20 12 20 22 26 28 M26 6 C32 12 32 22 26 28" fill="none" stroke="#6b6e72" stroke-width="2"/></svg>
      </div>
    </div>
  </section>

  <section class="side side--back">
    <div class="wall-backdrop" role="img" aria-label="Faint photograph of concrete stairs on a light grey wall"></div>

    <div class="brand">
      <span class="brand__mark"></span>
      <div>
        <div class="brand__name">LANTERNWELL GROUP</div>
        <div class="brand__tagline">BUSINESS ADVISORS &amp; ACCOUNTANTS</div>
      </div>
    </div>

    <h2 class="services-title">OUR SERVICES</h2>
    <ul class="services services--left">
      <li>Taxation Compliance</li>
      <li>Financial &amp; Management Reporting</li>
      <li>Self-Managed Superannuation</li>
      <li>Virtual CFO</li>
      <li>Business Planning</li>
      <li>KPIs &amp; Performance Monitoring</li>
      <li>Succession Planning</li>
    </ul>
    <ul class="services services--right">
      <li>Estate Planning</li>
      <li>Cloud Solutions</li>
      <li>Business Support Services</li>
      <li>The Wine Industry</li>
    </ul>

    <div class="accent-bar"></div>
    <div class="advisor-photo" role="img" aria-label="Photograph of a smiling young advisor in a dark suit and green tie holding a folder"></div>

    <div class="contact">
      <div class="contact__row">0400 318 762
        <svg class="contact__icon" viewBox="0 0 40 30" aria-hidden="true"><path d="M8 28 A16 16 0 0 1 30 4" fill="none" stroke="#6b6e72" stroke-width="3"/><path d="M20 24 L26 8 L31 10 L28 13 L24 22 Z" fill="#6b6e72"/></svg>
      </div>
      <div class="contact__row">www.lanternwellgroup.com.au
        <svg class="contact__icon" viewBox="0 0 40 30" aria-hidden="true"><path d="M8 29 A16 16 0 0 1 24 3" fill="none" stroke="#6b6e72" stroke-width="3"/><circle cx="26" cy="17" r="11" fill="none" stroke="#6b6e72" stroke-width="2.5"/><path d="M15 17 H37 M26 6 V28 M26 6 C20 12 20 22 26 28 M26 6 C32 12 32 22 26 28" fill="none" stroke="#6b6e72" stroke-width="2"/></svg>
      </div>
    </div>
  </section>

</main>
</body>
</html>
```